I want to create a postcard we can use as a promotional offer. We may send out to prospects or give to people at an event to get them in front of us and start to understand their business more with the hope of engaging them as clients eventually.
The offer is a Complimentary "Pathwise Launch Pack". (valued at $875)
The kit includes:
Finance Prism Review
45 minute Business Discovery Meeting
6 point Diagnostic Report
3 Recommendations for your Business

The headline and there look and feel we would like the design to be focused upon is "Analyze. Boost. Grow."
Include an Image(s) as you feel appropriate.
I'm thinking Headline/Mian Branding and Picture on the Front, then Offer and details of Kit and Logos etc on the Back.

Include 2 logos as we are part of a joint operation, Meridel Accountants & Trovandel.

Call to action to Phone 0255501842 or email hello@trovandel.example.com.au

Logo's uploaded, committed payment, increased deadline.

Target Market(s)

Small to Medium Business

Industry/Entity Type

Business

Requirements
Must have
• Logos in Colour on Back with rest of Detail.
Front to be all about the key message "Analyze. Boost. Grow." select pic to represent.
Must create cut through and intrigue to make the holder tunr the card and read.

```html
<!DOCTYPE html>
<html lang="en">
<head>
<meta charset="utf-8">
<title>Pathwise Launch Pack Postcard</title>
<link rel="stylesheet" href="https://fonts.googleapis.com/css2?family=Exo+2:wght@600;700&family=Source+Sans+3:wght@400;600;700&display=swap">
<style>
  :root {
    --page: #eef0f2;
    --card: #ffffff;
    --navy: #15233f;
    --ink: #1c2230;
    --green-light: #c4e06a;
    --green: #8cc63f;
    --green-dark: #5c8a1e;
    --panel-top: #e9ebee;
    --panel-bottom: #ffffff;
    --offer-blue: #1f6fa0;
    --offer-green: #4e9a2c;
    --rule: #8d9096;
    --photo-dark: #0c1220;
    --photo-mid: #2a3550;
    --photo-warm: #c89a7a;
  }
  * { box-sizing: border-box; margin: 0; padding: 0; }
  html, body { width: 1116px; height: 1200px; overflow: hidden; }
  body { background: var(--page); position: relative; font-family: "Source Sans 3", Arial, sans-serif; }

  /* ---------- Front ---------- */
  .card-front {
    position: absolute; left: 132px; top: 34px; width: 680px; height: 524px;
    background: var(--photo-dark); overflow: visible;
  }
  .front-photo {
    position: absolute; inset: 0;
    background:
      radial-gradient(ellipse 34% 40% at 50% 66%, var(--photo-warm) 0%, rgba(200,154,122,0.35) 55%, transparent 80%),
      radial-gradient(ellipse 70% 80% at 50% 55%, var(--photo-mid) 0%, var(--photo-dark) 75%);
  }
  .headline-ribbon {
    position: absolute; left: 0; top: 26px; width: 680px; height: 74px;
    background: linear-gradient(180deg, var(--green-light) 0%, var(--green) 100%);
    display: flex; align-items: center; justify-content: center;
  }
  .headline-ribbon .fold {
    position: absolute; top: 74px; width: 0; height: 0;
    border-top: 16px solid var(--green-dark);
  }
  .headline-ribbon .fold-left { left: 0; border-left: 18px solid transparent; }
  .headline-ribbon .fold-right { right: 0; border-right: 18px solid transparent; }
  .headline {
    font-family: "Exo 2", Arial, sans-serif; font-weight: 700; font-size: 46px;
    color: var(--navy); letter-spacing: 2px; white-space: nowrap;
  }
  .headline .sep { font-size: 26px; vertical-align: middle; margin: 0 10px; }

  /* ---------- Back ---------- */
  .card-back {
    position: absolute; left: 271px; top: 596px; width: 825px; height: 572px;
    background: var(--card); box-shadow: 0 0 0 1px #d9dce0;
  }
  .offer-panel {
    position: absolute; left: 0; top: 0; width: 347px; height: 572px;
    background: linear-gradient(180deg, var(--panel-top) 0%, #d6d9dd 45%, var(--panel-bottom) 100%);
  }
  .kit-ribbon {
    position: absolute; left: 0; top: 30px; width: 357px; height: 54px;
    background: linear-gradient(180deg, var(--green-light) 0%, var(--green) 100%);
    display: flex; align-items: center; padding-left: 24px;
  }
  .kit-ribbon .fold {
    position: absolute; right: 0; top: 54px; width: 0; height: 0;
    border-top: 12px solid var(--green-dark); border-right: 10px solid transparent;
  }
  .kit-title {
    font-family: "Exo 2", Arial, sans-serif; font-weight: 600; font-size: 25px;
    color: var(--navy); text-transform: uppercase; letter-spacing: 0.5px; white-space: nowrap;
  }
  .kit-contents { position: absolute; left: 30px; top: 128px; color: var(--ink); }
  .kit-contents h2 { font-size: 18px; font-weight: 700; margin-bottom: 6px; text-transform: uppercase; }
  .kit-contents li { list-style: none; font-size: 17px; font-weight: 600; line-height: 30px; }
  .kit-contents li::before { content: "» "; }
  .feature-icons { position: absolute; left: 62px; top: 300px; display: flex; gap: 22px; }
  .feature-icons svg { width: 46px; height: 46px; }
  .contact { position: absolute; left: 30px; top: 380px; font-size: 17px; font-weight: 600; color: var(--ink); line-height: 30px; }
  .partners { position: absolute; left: 26px; top: 470px; display: flex; align-items: center; gap: 22px; }
  .partner-name { font-size: 22px; font-weight: 700; color: var(--navy); display: flex; align-items: center; gap: 6px; }
  .partner-name .mark { width: 16px; height: 16px; border-radius: 50%; background: var(--green); }

  .offer-label { position: absolute; left: 400px; top: 58px; text-align: center; }
  .offer-label .free { font-size: 22px; font-weight: 700; color: var(--offer-blue); text-transform: uppercase; }
  .offer-label .value { font-size: 17px; font-weight: 600; color: var(--offer-green); }
  .stamp-box { position: absolute; left: 542px; top: 27px; width: 113px; height: 113px; border: 1.5px solid var(--rule); }
  .address-line { position: absolute; left: 419px; width: 237px; height: 0; border-top: 1.5px solid var(--rule); }
</style>
</head>
<body>

<section class="card-front">
  <div class="front-photo" role="img" aria-label="Photo of hands in a dark suit cupping soil with a young green seedling"></div>
  <div class="headline-ribbon">
    <span class="fold fold-left"></span>
    <h1 class="headline">ANALYZE<span class="sep">»</span>BOOST<span class="sep">»</span>GROW</h1>
    <span class="fold fold-right"></span>
  </div>
</section>

<section class="card-back">
  <div class="offer-panel">
    <div class="kit-ribbon">
      <span class="kit-title">Pathwise Launch Pack</span>
      <span class="fold"></span>
    </div>

    <div class="kit-contents">
      <h2>The kit includes:</h2>
      <ul>
        <li>Finance Prism Review</li>
        <li>Business Discovery Meeting</li>
        <li>6 point Diagnostic Report</li>
        <li>3 Recommendations for your Business</li>
      </ul>
    </div>

    <div class="feature-icons">
      <svg viewBox="0 0 46 46"><circle cx="23" cy="23" r="22" fill="#1f6d8a"/><path d="M14 24l6 6 12-14" stroke="#fff" stroke-width="3.5" fill="none" stroke-linecap="round" stroke-linejoin="round"/></svg>
      <svg viewBox="0 0 46 46"><circle cx="23" cy="23" r="22" fill="#3f8f3a"/><circle cx="23" cy="23" r="9" fill="none" stroke="#fff" stroke-width="3"/></svg>
      <svg viewBox="0 0 46 46"><circle cx="23" cy="23" r="22" fill="#2d8a7a"/><rect x="15" y="15" width="16" height="16" rx="2" fill="none" stroke="#fff" stroke-width="3"/></svg>
      <svg viewBox="0 0 46 46"><circle cx="23" cy="23" r="22" fill="#4f9d3c"/><path d="M13 28l7-7 5 5 8-9" stroke="#fff" stroke-width="3" fill="none" stroke-linecap="round" stroke-linejoin="round"/></svg>
    </div>

    <div class="contact">
      <p>Phone: 0255501842</p>
      <p>email: hello@trovandel.example.com.au</p>
    </div>

    <div class="partners">
      <span class="partner-name">Meridel</span>
      <span class="partner-name"><span class="mark"></span>Trovandel</span>
    </div>
  </div>

  <div class="offer-label">
    <p class="free">Free offer</p>
    <p class="value">valued at $875</p>
  </div>
  <div class="stamp-box"></div>
  <div class="address-line" style="top:215px"></div>
  <div class="address-line" style="top:265px"></div>
  <div class="address-line" style="top:316px"></div>
</section>

</body>
</html>
```